Dell Brunow for Columbia County Commissioner

3"x12" sized bumper sticker design based on the provided logo.

Please also include Vote November 4 or just November 4 somewhere in the design.

```html
<!DOCTYPE html>
<html lang="en">
<head>
<meta charset="utf-8">
<title>Dell Brunow – Columbia County Commissioner</title>
<link rel="stylesheet" href="https://fonts.googleapis.com/css2?family=Cinzel:wght@400;500&family=PT+Sans:wght@700&display=swap">
<style>
  :root {
    --navy: #1b2254;
    --navy-deep: #141a44;
    --red: #e01e2a;
    --red-dark: #8e0f17;
    --white: #ffffff;
    --gold: #d9b85a;
    --gold-light: #f4e3a6;
  }
  html, body {
    margin: 0;
    padding: 0;
    width: 1200px;
    height: 300px;
    overflow: hidden;
    background: var(--white);
  }
  .sticker {
    position: relative;
    width: 1200px;
    height: 300px;
    overflow: hidden;
    background: var(--navy);
  }
  .sticker-art {
    position: absolute;
    inset: 0;
  }
  .candidate-name {
    position: absolute;
    left: 55px;
    top: 22px;
    width: 500px;
    margin: 0;
    color: var(--white);
    font-family: "Cinzel", "Times New Roman", serif;
    font-weight: 400;
    text-align: center;
    line-height: 1;
  }
  .candidate-name .first {
    display: block;
    font-size: 60px;
    letter-spacing: 1px;
  }
  .candidate-name .last {
    display: block;
    font-size: 96px;
    letter-spacing: 0;
    margin-top: -4px;
  }
  .office {
    position: absolute;
    left: 570px;
    top: 82px;
    width: 510px;
    margin: 0;
    color: var(--white);
    font-family: "Cinzel", "Times New Roman", serif;
    font-weight: 400;
    text-align: center;
    line-height: 1;
  }
  .office .county {
    display: block;
    font-size: 30px;
    letter-spacing: 6px;
  }
  .office .title {
    display: block;
    font-size: 46px;
    letter-spacing: 5px;
    margin-top: 8px;
  }
  .vote-ribbon-text {
    font-family: "PT Sans", Arial, sans-serif;
    font-weight: 700;
    fill: var(--white);
  }
</style>
</head>
<body>
<div class="sticker">
  <svg class="sticker-art" viewBox="0 0 1200 300" width="1200" height="300" aria-hidden="true">
    <defs>
      <linearGradient id="swoosh-red" x1="0" y1="0" x2="1" y2="0">
        <stop offset="0" stop-color="var(--red)"/>
        <stop offset="0.55" stop-color="var(--red)"/>
        <stop offset="1" stop-color="var(--red-dark)"/>
      </linearGradient>
      <linearGradient id="star-gold" x1="0" y1="0" x2="0" y2="1">
        <stop offset="0" stop-color="var(--gold-light)"/>
        <stop offset="1" stop-color="var(--gold)"/>
      </linearGradient>
      <linearGradient id="ribbon-red" x1="0" y1="0" x2="1" y2="1">
        <stop offset="0" stop-color="var(--red)"/>
        <stop offset="1" stop-color="var(--red-dark)"/>
      </linearGradient>
      <symbol id="star" viewBox="-10 -10 20 20">
        <polygon points="0,-10 2.35,-3.24 9.51,-3.09 3.8,1.24 5.88,8.09 0,4 -5.88,8.09 -3.8,1.24 -9.51,-3.09 -2.35,-3.24" fill="url(#star-gold)"/>
      </symbol>
    </defs>

    <!-- navy field -->
    <rect class="field" width="1200" height="300" fill="var(--navy)"/>

    <!-- red swoosh -->
    <path class="swoosh-red" d="M0,200 C320,198 720,190 1200,140 L1200,178 C800,210 400,218 0,216 Z" fill="url(#swoosh-red)"/>

    <!-- white base -->
    <path class="base-white" d="M0,214 C400,218 800,204 1200,172 L1200,300 L0,300 Z" fill="var(--white)"/>

    <!-- navy stripes -->
    <path class="stripe" d="M0,234 C400,240 800,226 1200,196 L1200,214 C800,246 400,256 0,250 Z" fill="var(--navy)"/>
    <path class="stripe" d="M0,266 C400,273 800,259 1200,230 L1200,247 C800,279 400,289 0,282 Z" fill="var(--navy)"/>
    <path class="stripe" d="M0,296 C400,302 800,292 1200,266 L1200,300 L0,300 Z" fill="var(--navy)"/>

    <!-- star row -->
    <g class="star-row">
      <use href="#star" x="678" y="34" width="44" height="44"/>
      <use href="#star" x="738" y="34" width="44" height="44"/>
      <use href="#star" x="798" y="34" width="44" height="44"/>
      <use href="#star" x="858" y="34" width="44" height="44"/>
      <use href="#star" x="918" y="34" width="44" height="44"/>
    </g>

    <!-- vote ribbon -->
    <g class="vote-ribbon">
      <polygon points="1000,0 1100,0 1200,100 1200,200" fill="url(#ribbon-red)"/>
      <line x1="1000" y1="0" x2="1200" y2="200" stroke="var(--gold)" stroke-width="4"/>
      <line x1="1100" y1="0" x2="1200" y2="100" stroke="var(--gold)" stroke-width="4"/>
      <text class="vote-ribbon-text" transform="translate(1138,62) rotate(45)" text-anchor="middle" font-size="26">VOTE</text>
      <text class="vote-ribbon-text" transform="translate(1114,88) rotate(45)" text-anchor="middle" font-size="22">November 4</text>
    </g>
  </svg>

  <h1 class="candidate-name">
    <span class="first">DELL</span>
    <span class="last">BRUNOW</span>
  </h1>

  <p class="office">
    <span class="county">COLUMBIA COUNTY</span>
    <span class="title">COMMISSIONER</span>
  </p>
</div>
</body>
</html>
```